World Wide News and Current Affairs website

We intends to start up a new website which deals on New and Current Affairs.
Attention Designers,
We want a home page design for this project. Our business is based in the United States. Our goal is to become a well known brand.
The website would consist of a category for News, Business and Tech.
The theme should be beautiful and attention seeking. The website would take bulk of it's news from the US, and Europe.
Designers can get inspiration from already existing new websites such as ZPW, VJL, HALDRIM.
All designs should be clean and easy to navigate.

```html
<!DOCTYPE html>
<html lang="en">
<head>
<meta charset="utf-8">
<title>Norvale News</title>
<link href="https://fonts.googleapis.com/css2?family=Oswald:wght@400;500&family=Open+Sans:wght@400;600;700&display=swap" rel="stylesheet">
<style>
:root{
  --bar:#2a2a2a;
  --ink:#222;
  --muted:#555;
  --soft:#e9e9e9;
  --panel:#f6f6f6;
  --accent:#f0652a;
  --date:#e8663c;
  --footer:#464646;
  --white:#fff;
  --rule:#cfcfcf;
}
*{box-sizing:border-box;margin:0;padding:0}
html,body{width:1200px;height:3863px;overflow:hidden}
body{position:relative;background:var(--white);font-family:"Open Sans",Arial,sans-serif;color:var(--ink)}
.abs{position:absolute}
.ph{position:absolute;display:block}
.site-header{left:0;top:0;width:1200px;height:82px;background:var(--bar)}
.brand{left:98px;top:24px;color:var(--white);font-family:"Oswald",sans-serif;font-size:24px;font-weight:500;letter-spacing:.5px}
.main-nav{left:362px;top:30px;display:flex}
.main-nav a{color:#ddd;font-size:15px;text-decoration:none;margin-right:40px}
.search{left:938px;top:22px;width:162px;height:38px;border:1px solid #888;color:#ccc;font-size:14px;padding:9px 10px}
.search svg{position:absolute;right:10px;top:11px}
.hero{left:0;top:82px;width:1200px;height:490px;background:var(--soft)}
.tile-caption{color:var(--white)}
.tile-caption h2{font-family:"Oswald",sans-serif;font-weight:500;letter-spacing:.5px}
.tile-caption p{font-size:14px;line-height:21px;margin-top:8px}
.section-title{left:0;width:1200px;text-align:center;font-family:"Oswald",sans-serif;font-size:30px;font-weight:400;color:var(--ink)}
.section-title span{background:var(--white);padding:0 30px;position:relative}
.section-title:before{content:"";position:absolute;left:250px;right:250px;top:50%;height:1px;background:var(--rule)}
.intro{left:98px;top:732px;width:1004px;text-align:center;font-size:13px;line-height:21px;color:var(--muted)}
.card-label{position:absolute;left:14px;width:204px;top:234px;height:104px;background:var(--white);border:1px solid #d8d8d8;text-align:center;padding-top:14px}
.card-label h3{font-size:15px;font-weight:600;margin-bottom:12px}
.card-label p{font-size:12px;line-height:19px;color:var(--muted);padding:0 14px}
.card-label.dark{background:#444;border-color:#444;color:var(--white)}
.card-label.dark p{color:#ddd}
.main{left:98px;top:1226px;width:1004px;height:1498px;background:var(--panel)}
.col-title{font-family:"Oswald",sans-serif;font-size:26px;color:var(--ink)}
.col-title:after{content:"";display:block;width:55px;height:2px;background:var(--ink);margin-top:10px}
.story-tag{position:absolute;left:0;bottom:22px;background:rgba(30,30,30,.75);color:var(--white);font-size:16px;font-weight:600;padding:10px 12px;width:220px}
.meta{font-size:11px;color:var(--date);display:flex;gap:24px}
.excerpt{font-size:11px;line-height:18px;color:var(--muted);margin-top:8px}
.read-more{display:inline-block;margin-top:14px;background:#333;color:var(--white);font-size:12px;font-weight:600;padding:7px 14px}
.play{position:absolute;left:50%;top:50%;transform:translate(-50%,-50%)}
.side-title{width:310px;text-align:center;font-size:19px;font-weight:600}
.pick p{font-size:13px;line-height:20px;margin-top:14px;width:236px}
.pick .date{color:var(--date);font-size:12px;margin-top:10px}
.dot{display:inline-block;border-radius:50%}
.pic-caption{position:absolute;left:20px;bottom:18px;color:var(--white)}
.pic-caption h4{font-family:"Oswald",sans-serif;font-weight:400;font-size:19px;letter-spacing:.3px}
.pic-caption span{font-size:13px;display:block;margin-top:4px}
.site-footer{left:0;top:3540px;width:1200px;height:323px;background:var(--footer);color:var(--white)}
.foot-nav{left:0;width:1200px;top:180px;text-align:center;font-size:15px;font-weight:600;letter-spacing:.5px}
.foot-nav span{margin:0 18px}
</style>
</head>
<body>

<header class="site-header abs">
  <div class="brand abs">NORVALE NEWS</div>
  <nav class="main-nav abs"><a>News</a><a>Sports</a><a>Weather</a><a>Shop</a><a>Earth</a><a>Travel</a><a>More</a></nav>
  <div class="search abs">Search
    <svg width="16" height="16" viewBox="0 0 16 16"><circle cx="6.5" cy="6.5" r="5" fill="none" stroke="#ddd" stroke-width="2"/><line x1="10" y1="10" x2="15" y2="15" stroke="#ddd" stroke-width="2"/></svg>
  </div>
</header>

<section class="hero abs">
  <div class="ph" style="left:98px;top:42px;width:605px;height:404px;background:linear-gradient(135deg,#8a7f73,#4b4640 60%,#2e2b28)" role="img" aria-label="Man reading a newspaper on a city street"></div>
  <div class="tile-caption abs" style="left:121px;top:318px;width:520px">
    <h2 style="font-size:28px">NORVALE TOP NEWS</h2>
    <p>Nemo enim ipsam voluptatem quia voluptas sit aspernatur aut odit aut fugit, sed quia consequuntur.</p>
  </div>
  <div class="ph" style="left:718px;top:42px;width:382px;height:195px;background:linear-gradient(135deg,#9a9a96,#4c4c4a)" role="img" aria-label="Hand holding a tablet showing news"></div>
  <div class="tile-caption abs" style="left:736px;top:164px;width:340px">
    <h2 style="font-size:17px">WESTERN CIVILISATION</h2>
    <p style="font-size:12px;margin-top:4px">Nemo enim ipsam voluptatem quia voluptas sit</p>
  </div>
  <div class="ph" style="left:718px;top:253px;width:382px;height:193px;background:linear-gradient(135deg,#a69c92,#54504c)" role="img" aria-label="People reading newspapers"></div>
  <div class="tile-caption abs" style="left:736px;top:370px;width:340px">
    <h2 style="font-size:17px">NEWS UPTO DATE</h2>
    <p style="font-size:12px;margin-top:4px">Nemo enim ipsam voluptatem quia voluptas sit</p>
  </div>
</section>

<h2 class="section-title abs" style="top:655px"><span>TOP RATED NEWS</span></h2>
<p class="intro abs">Nemo enim ipsam voluptatem quia voluptas sit aspernatur aut odit aut fugit, sed quia consequuntur magni dolores eos qui ratione voluptatem sequi nesciunt. Neque porro quisquam est, qui dolorem ipsum quia dolor sit amet, consectetur.</p>

<div class="abs" style="left:108px;top:816px;width:232px;height:340px">
  <div class="ph" style="left:0;top:0;width:232px;height:256px;background:linear-gradient(135deg,#3f8f8a,#5a4b44)" role="img" aria-label="Reporters holding microphones"></div>
  <div class="card-label"><h3>US POLICE ATTACK</h3><p>Sed ut perspiciatis unde omnis iste natus.</p></div>
</div>
<div class="abs" style="left:358px;top:816px;width:232px;height:340px">
  <div class="ph" style="left:0;top:0;width:232px;height:256px;background:linear-gradient(135deg,#c9a77f,#7b5a3e)" role="img" aria-label="Woman reading a newspaper"></div>
  <div class="card-label dark"><h3>PUBLIC NEWS</h3><p>Sed ut perspiciatis unde omnis iste natus.</p></div>
</div>
<div class="abs" style="left:608px;top:816px;width:232px;height:340px">
  <div class="ph" style="left:0;top:0;width:232px;height:256px;background:linear-gradient(135deg,#c8c8c8,#56585c)" role="img" aria-label="Man in a suit speaking to microphones"></div>
  <div class="card-label"><h3>PARLIAMENT NEWS</h3><p>Sed ut perspiciatis unde omnis iste natus.</p></div>
</div>
<div class="abs" style="left:858px;top:816px;width:232px;height:340px">
  <div class="ph" style="left:0;top:0;width:232px;height:256px;background:linear-gradient(135deg,#b5b2a8,#5d5a50)" role="img" aria-label="Crowd gathered around a speaker outdoors"></div>
  <div class="card-label"><h3>LEADERS DEAL</h3><p>Sed ut perspiciatis unde omnis iste natus.</p></div>
</div>

<main class="main abs">
  <h2 class="col-title abs" style="left:20px;top:18px">INDIA NEWS</h2>

  <article class="abs" style="left:20px;top:90px;width:309px">
    <div style="position:relative;height:229px;background:linear-gradient(135deg,#8b6a50,#3e3028)" role="img" aria-label="People reading news in a cafe"><div class="story-tag">News Readers</div></div>
    <div class="meta" style="margin-top:22px"><span>Posted: 09-2-16</span><span>Last Modified: 10-2-16</span></div>
    <p class="excerpt">Nemo enim ipsam voluptatem quia voluptas sit aspernatur aut odit aut fugit, sed quia consequuntur magni dolores eos qui ratione voluptatem sequi nesciunt.</p>
    <span class="read-more">Read More</span>
  </article>
  <article class="abs" style="left:352px;top:90px;width:309px">
    <div style="position:relative;height:229px;background:linear-gradient(135deg,#b9c4cc,#5f6a72)" role="img" aria-label="Man reading a newspaper by a window"><div class="story-tag">News Ideas</div></div>
    <div class="meta" style="margin-top:22px"><span>Posted: 09-2-16</span><span>Last Modified: 10-2-16</span></div>
    <p class="excerpt">Nemo enim ipsam voluptatem quia voluptas sit aspernatur aut odit aut fugit, sed quia consequuntur magni dolores eos qui ratione voluptatem sequi nesciunt.</p>
    <span class="read-more">Read More</span>
  </article>
  <article class="abs" style="left:20px;top:507px;width:309px">
    <div style="position:relative;height:229px;background:linear-gradient(135deg,#d0d0d0,#2f2f2f)" role="img" aria-label="Camera crews and microphones at a press event"><div class="story-tag">Inspirations</div></div>
    <div class="meta" style="margin-top:22px"><span>Posted: 09-2-16</span><span>Last Modified: 10-2-16</span></div>
    <p class="excerpt">Nemo enim ipsam voluptatem quia voluptas sit aspernatur aut odit aut fugit, sed quia consequuntur magni dolores eos qui ratione voluptatem sequi nesciunt.</p>
    <span class="read-more">Read More</span>
  </article>
  <article class="abs" style="left:352px;top:507px;width:309px">
    <div style="position:relative;height:229px;background:linear-gradient(135deg,#9c7a5c,#3a2e26)" role="img" aria-label="Person watching a laptop on a wooden desk"><div class="story-tag">Spirit of Watching</div></div>
    <div class="meta" style="margin-top:22px"><span>Posted: 09-2-16</span><span>Last Modified: 10-2-16</span></div>
    <p class="excerpt">Nemo enim ipsam voluptatem quia voluptas sit aspernatur aut odit aut fugit, sed quia consequuntur magni dolores eos qui ratione voluptatem sequi nesciunt.</p>
    <span class="read-more">Read More</span>
  </article>

  <h2 class="col-title abs" style="left:20px;top:960px">OUR VIDEO BLOG</h2>
  <div class="ph" style="left:20px;top:1045px;width:639px;height:272px;background:linear-gradient(120deg,#3b2a22,#1d3a4a 60%,#2d5a6c)" role="img" aria-label="Street at night with a large illuminated billboard">
    <svg class="play" width="64" height="64" viewBox="0 0 64 64"><circle cx="32" cy="32" r="29" fill="none" stroke="#fff" stroke-width="4"/><path d="M26 19 L46 32 L26 45Z" fill="#fff"/></svg>
  </div>
  <div class="ph" style="left:20px;top:1331px;width:201px;height:152px;background:linear-gradient(135deg,#8a8378,#3d3a35)" role="img" aria-label="Hands holding a newspaper">
    <svg class="play" width="42" height="42" viewBox="0 0 64 64"><circle cx="32" cy="32" r="29" fill="none" stroke="#fff" stroke-width="5"/><path d="M26 19 L46 32 L26 45Z" fill="#fff"/></svg>
  </div>
  <div class="ph" style="left:239px;top:1331px;width:201px;height:152px;background:linear-gradient(135deg,#8ea0b4,#3e4a58)" role="img" aria-label="Microphones at a press conference">
    <svg class="play" width="42" height="42" viewBox="0 0 64 64"><circle cx="32" cy="32" r="29" fill="none" stroke="#fff" stroke-width="5"/><path d="M26 19 L46 32 L26 45Z" fill="#fff"/></svg>
  </div>
  <div class="ph" style="left:458px;top:1331px;width:201px;height:152px;background:linear-gradient(135deg,#5f7ea0,#30384a)" role="img" aria-label="Remote control pointed at a television">
    <svg class="play" width="42" height="42" viewBox="0 0 64 64"><circle cx="32" cy="32" r="29" fill="none" stroke="#fff" stroke-width="5"/><path d="M26 19 L46 32 L26 45Z" fill="#fff"/></svg>
  </div>

  <aside class="abs" style="left:692px;top:0;width:312px;height:1498px;background:#f9f9f9">
    <h3 class="side-title abs" style="top:22px;left:0">Editor's Picks</h3>
    <div class="pick abs" style="left:37px;top:61px">
      <div style="width:236px;height:155px;background:linear-gradient(135deg,#d8d6d0,#6e6b64)" role="img" aria-label="Stack of newspapers"></div>
      <p>Nemo enim ipsam voluptatem quia voluptas sit aspernatur.</p><div class="date">&#9711; September 25, 2015</div>
    </div>
    <div class="pick abs" style="left:37px;top:326px">
      <div style="width:236px;height:155px;background:linear-gradient(135deg,#b0533c,#3a3f48)" role="img" aria-label="Laptop and coffee on a desk"></div>
      <p>Nemo enim ipsam voluptatem quia voluptas sit aspernatur.</p><div class="date">&#9711; September 25, 2015</div>
    </div>
    <div class="pick abs" style="left:37px;top:591px">
      <div style="width:236px;height:155px;background:linear-gradient(135deg,#a0705a,#4a342a)" role="img" aria-label="Man reading a newspaper"></div>
      <p>Nemo enim ipsam voluptatem quia voluptas sit aspernatur.</p><div class="date">&#9711; September 25, 2015</div>
    </div>
    <div class="abs" style="left:37px;top:862px;width:236px;height:1px;background:var(--rule)"></div>
    <h3 class="side-title abs" style="top:889px;font-size:16px">SOCIAL MEDIA</h3>
    <div class="abs" style="left:56px;top:948px;display:flex;gap:8px">
      <span class="dot" style="width:34px;height:34px;background:#3b5a98"></span>
      <span class="dot" style="width:34px;height:34px;background:#3a9fe0"></span>
      <span class="dot" style="width:34px;height:34px;background:#dd4b39"></span>
      <span class="dot" style="width:34px;height:34px;background:#1f7bb6"></span>
      <span class="dot" style="width:34px;height:34px;background:#e0362b"></span>
    </div>
    <div class="abs" style="left:37px;top:1009px;width:236px;height:1px;background:var(--rule)"></div>
    <h3 class="side-title abs" style="top:1035px;font-size:16px">SUBSCRIBE</h3>
    <div class="abs" style="left:37px;top:1071px;width:236px;height:44px;background:var(--white);border:1px solid #ccc;font-size:12px;color:#888;padding:13px 10px">Email Address</div>
    <div class="abs" style="left:37px;top:1130px;width:236px;height:44px;background:var(--accent);color:var(--white);font-size:15px;font-weight:600;text-align:center;line-height:44px">SUBSCRIBE</div>
    <div class="ph" style="left:37px;top:1194px;width:236px;height:284px;background:linear-gradient(160deg,#4a5f78,#26313f)" role="img" aria-label="People reading news"></div>
    <div class="abs" style="left:47px;top:1206px;color:var(--white);font-size:14px;font-weight:600">IN THE NEWS</div>
  </aside>
</main>

<h2 class="section-title abs" style="top:2803px"><span>WORLD IN PICTURES</span></h2>

<div class="ph" style="left:98px;top:2902px;width:492px;height:296px;background:linear-gradient(135deg,#c9c6c0,#7c766c)" role="img" aria-label="Photographer in front of a white domed monument">
  <div class="pic-caption"><h4>WORLD PHOTOGRAPHY AWARDS 2017</h4><span>In Pictures</span></div></div>
<div class="ph" style="left:610px;top:2902px;width:490px;height:296px;background:linear-gradient(135deg,#5e5a56,#a89c90)" role="img" aria-label="Camera crew filming a presenter">
  <div class="pic-caption"><h4>TOP RATED NEWS</h4><span>In Pictures</span></div></div>
<div class="ph" style="left:98px;top:3226px;width:319px;height:237px;background:linear-gradient(135deg,#6b7680,#2e3338)" role="img" aria-label="People meeting in an office">
  <div class="pic-caption"><h4>TEMPORA INCIDUNT</h4><span>In Pictures</span></div></div>
<div class="ph" style="left:440px;top:3226px;width:320px;height:237px;background:linear-gradient(135deg,#8a5a40,#2e241e)" role="img" aria-label="Man with a coffee cup">
  <div class="pic-caption"><h4>DOLOREMQUE LAUDANTIUM</h4><span>In Pictures</span></div></div>
<div class="ph" style="left:780px;top:3226px;width:320px;height:237px;background:linear-gradient(135deg,#7a6a60,#2c2a2e)" role="img" aria-label="Speaker surrounded by microphones">
  <div class="pic-caption"><h4>VOLUPTATEM ACCUSANTIUM</h4><span>In Pictures</span></div></div>

<footer class="site-footer abs">
  <div class="abs" style="left:0;width:1200px;top:76px;text-align:center;font-family:'Oswald',sans-serif;font-size:30px;font-weight:500;letter-spacing:.5px">NORVALE NEWS</div>
  <nav class="foot-nav abs"><span>NEWS</span>|<span>SPORT</span>|<span>WEATHER</span>|<span>SHOP</span>|<span>EARTH</span>|<span>TRAVEL</span>|<span>CULTURE</span></nav>
  <div class="abs" style="left:98px;top:225px;width:1004px;height:1px;background:#888"></div>
  <div class="abs" style="left:98px;top:272px;font-size:12px;color:#ddd">Copyrights © 2017 Norvale News. All Rights Reserved</div>
  <div class="abs" style="left:910px;top:260px;display:flex;gap:6px">
    <span class="dot" style="width:32px;height:32px;border:2px solid #ddd"></span>
    <span class="dot" style="width:32px;height:32px;border:2px solid #ddd"></span>
    <span class="dot" style="width:32px;height:32px;border:2px solid #ddd"></span>
    <span class="dot" style="width:32px;height:32px;border:2px solid #ddd"></span>
    <span class="dot" style="width:32px;height:32px;border:2px solid #ddd"></span>
  </div>
</footer>

</body>
</html>
```